" Visao Travolend Visão Ser reconhecida como uma empresa de referência em consultoria na área de Tecnologias e sistemas de informação pelas empresas angolanas, tanto no ponto de vista tecnológico, como no ponto de vista da qualidade e da etica, respondendo com excelência todas as solicitações de clientes, seja de entidades particulares ou publicas; Missão • Prestar serviços de consultoria de acordo as boas praticas e a norma internacionais para melhorar a sua qualidade interna; • Gerar e entregar valor com as nossas soluções; • Oferecer um serviço consultoria e de tecnologia personalizadas, com inovação e segurança, com responsabilidade social e a etica; • Responder em tempo util todas as solicitações de clientes; Valores A Travolend tem como valores: • Rigor no cumprimento dos procedimentos operacional padrão que resultará na qualidade interna; • Integridade na relação com os seus clientes; • Qualidade com Adesão à certificação IS0 20000; • Comprometimento com a comunidade, ambiente e etica; • Inovação continua. SERVIÇOS OU AREAS DE ACTUAÇÃO IT/SI Consulting/Advisory - Governança de TI (Cobit/ValIT e Outros Standards) - Gestão de Serviços com ITIL e ISO 20000 - Assessments e Modelos Organizacionais de TI - Planos Estrategicos de TI - Demonstração do Valor da TI - Escritorio de Projetos de TI (PMO-TI) - Consultoria Estrategica e continuada - Alinhamento Estrategico de TI ao Negocio - Arquitecturas Tecnologicas (Sistemas e Serviços) - Gestão de Riscos de TI Business Consulting - Desenho e Gestão de Processos de Negocios (BPM) - Desenho e redesenho Organizacional - Escritorio de projetos - Transformação Digital Big data & Analitics - Desenho de Dashboards de produtividade - Pesquisa e Desenvolvimento - Analises de Dados - Data Warehouse Metodologias e praticas - Canvas Business Model - Design Thinking - Cobit e Val IT - ISO 20000 - Iso 9000 - ISO 33000 - ISO 2700X Como entregamos os nossos produtos e serviços Entregas Nossas entregas sempre contam com Produtos e documentação detalhada: - Diagnóstico da Situação Atual; - Demonstração de Valores e Business Case - Plano de Ação detalhado para os próximos anos, - Implementação com Programas e Projetos - Follow-up Abordagem para Area de tecnologia Nos últimos anos, as empresas têm feito grandes investimentos em estratégia de TI para manter-se à frente da concorrência e dar suporte ao crescimento. No panorama econômico atual, é difícil avaliar com precisão o valor gerado por TI e identificar as opções práticas que permitirão impulsionar o crescimento e, ao mesmo tempo, racionalizar os custos e melhorar o desempenho. Sem uma estratégia correta, muitas empresas embutiram uma enorme complexidade em sua infraestrutura de TI e acabaram por criar complexidade adicional nos negócios. Não é surpresa que muitos Gestores não consigam determinar ao certo o valor gerado por TI ou as razões para a escalada dos custos com tecnologia. Na Travolend,, trabalhamos de forma independente de qualquer produto específico e consideramos exclusivamente as necessidades dos nossos clientes em termos de estratégia, pessoas, Tecnologia e processos. Ouvimos a dor do cliente, desenhamos uma solução, demonstramos o valor agregado e entregamos a solução. A travolend adopta uma agenda específica para atacar estes problemas: • Estruturar TI/SI para estar alinha a estratégica corporativa e ser um enabler do negocio, por meio de iniciativas que geram maior eficiência e eficácia. • Ajudamos a reduzir custos e complexidade da TI/SI e, consequentemente, minimizar o risco e aumentar a flexibilidade da organização, • Aumentar a transparência dos custos e do desempenho de TI/SI. Isso permite que a empresa entenda o valor do que está comprando e facilita os trade-offs econômicos. • Desenvolver TI/SI como um negócio dentro de um negócio através da implementação de standard e praticas internacionais provadas. Principais áreas de Negocio Líder em consultoria de gestão, a Travolend trabalha com executivos de vários setores para dar suporte à definição de sua agenda estratégica de Negocios e de suporte tecnologico de formas a aumentar o índice de sucesso das iniciativas destes. Nossas principais áreas de expertise incluem: IT/SI Consulting/Advisory Business Consulting Big data & Analitics "

```html
<!DOCTYPE html>
<html lang="pt">
<head>
<meta charset="utf-8">
<title>Travolend Consultoria — Início</title>
<link href="https://fonts.googleapis.com/css2?family=Montserrat:wght@300;400;500;600;700&display=swap" rel="stylesheet">
<style>
  :root {
    --backdrop: #2b2b2d;
    --navy-deep: #0d1a33;
    --navy: #15294d;
    --navy-mid: #1f3a6b;
    --steel: #3a5685;
    --white: #ffffff;
    --text-dark: #14213d;
    --accent: #1e88e5;
    --nav-text: #dfe6f2;
  }
  * { box-sizing: border-box; margin: 0; padding: 0; }
  html, body {
    width: 1200px;
    height: 1200px;
    overflow: hidden;
    background: var(--backdrop);
    font-family: "Montserrat", sans-serif;
  }
  .site {
    position: absolute;
    left: 0;
    top: 268px;
    width: 1200px;
    height: 665px;
    overflow: hidden;
    background: var(--navy-deep);
  }
  .hero-backdrop {
    position: absolute;
    inset: 0 0 40px 0;
    background:
      radial-gradient(ellipse at 85% 15%, rgba(90,120,170,0.55), transparent 45%),
      radial-gradient(ellipse at 70% 75%, rgba(70,95,140,0.45), transparent 40%),
      radial-gradient(ellipse at 10% 80%, rgba(60,85,130,0.4), transparent 40%),
      linear-gradient(100deg, var(--navy-deep) 0%, var(--navy) 40%, var(--navy-mid) 75%, var(--steel) 100%);
  }
  .topbar {
    position: absolute;
    top: 0; left: 0; right: 0;
    height: 80px;
    display: flex;
    align-items: center;
    padding: 0 145px;
  }
  .brand {
    display: flex;
    align-items: center;
    gap: 12px;
    color: var(--white);
    font-weight: 600;
    font-size: 24px;
    letter-spacing: 1px;
    text-transform: uppercase;
  }
  .brand-mark {
    width: 22px; height: 22px;
    background: var(--white);
  }
  .main-nav {
    margin-left: auto;
    display: flex;
    align-items: center;
    gap: 20px;
    font-size: 15px;
    color: var(--nav-text);
  }
  .main-nav .is-active { color: var(--white); font-weight: 700; }
  .nav-cta {
    margin-left: 10px;
    background: var(--accent);
    color: var(--white);
    font-weight: 600;
    font-size: 14px;
    padding: 9px 18px;
    border-radius: 3px;
  }
  .hero-copy {
    position: absolute;
    left: 289px;
    top: 222px;
    color: var(--white);
  }
  .hero-title {
    font-weight: 600;
    font-size: 50px;
    line-height: 1.15;
    letter-spacing: -0.5px;
  }
  .hero-subtitle {
    font-weight: 300;
    font-size: 44px;
    line-height: 1.15;
  }
  .hero-actions {
    display: flex;
    gap: 16px;
    margin-top: 28px;
  }
  .btn {
    display: inline-flex;
    align-items: center;
    justify-content: center;
    height: 40px;
    padding: 0 26px;
    font-size: 15px;
    font-weight: 600;
    border-radius: 3px;
  }
  .btn-primary { background: var(--white); color: var(--text-dark); }
  .btn-outline { border: 2px solid var(--white); color: var(--white); }
  .slider-dots {
    position: absolute;
    left: 289px;
    top: 570px;
    display: flex;
    gap: 12px;
  }
  .slider-dots span {
    width: 10px; height: 10px;
    border-radius: 50%;
    background: rgba(255,255,255,0.7);
  }
  .slider-dots span.is-current { background: var(--white); }
  .next-section {
    position: absolute;
    left: 0; right: 0; bottom: 0;
    height: 40px;
    background: var(--white);
  }
</style>
</head>
<body>
  <main class="site">
    <div class="hero-backdrop" role="img" aria-label="Fotografia em tons de azul escuro: aperto de mãos sobre uma mesa de escritório com portátil e documentos"></div>

    <header class="topbar">
      <div class="brand"><span class="brand-mark"></span>Travolend</div>
      <nav class="main-nav">
        <span class="is-active">Início</span>
        <span>Quem Somos</span>
        <span>Áreas de Atuação</span>
        <span>Notícias</span>
        <span class="nav-cta">Fale Conosco</span>
      </nav>
    </header>

    <section class="hero-copy">
      <h1 class="hero-title">Consultoria em Sistemas</h1>
      <p class="hero-subtitle">e tecnologia da informação</p>
      <div class="hero-actions">
        <span class="btn btn-primary">Saiba Mais</span>
        <span class="btn btn-outline">Quem Somos</span>
      </div>
    </section>

    <div class="slider-dots">
      <span class="is-current"></span><span></span><span></span><span></span><span></span>
    </div>

    <div class="next-section"></div>
  </main>
</body>
</html>
```